Quillstone Ventures Wordpress Theme

My current wordpress is at: http://quillstoneventuers.blogspacehost.com/

I own the actual domain for mapping.

I'd like the look and feel to be like: http://brightlarchworks.com/

With the front page all black with my logo in the middle (see attached).

The colors should be consistent with my business cards (see attached)

I'd like it to be clean, simple and a little flashy.

Requirements
Must have
• space for intro video

Plug in ability in wordpress

Calendar of events

Clip Vault

```html
<!DOCTYPE html>
<html lang="en">
<head>
<meta charset="utf-8">
<title>Quillstone Ventures</title>
<link rel="stylesheet" href="https://fonts.googleapis.com/css2?family=Open+Sans:wght@400;600;700&family=PT+Sans:wght@400;700&family=Rokkitt:wght@400&family=Didact+Gothic&display=swap">
<style>
  :root {
    --black: #000000;
    --page: #0c0e10;
    --red: #a3001c;
    --red-dark: #6d0012;
    --red-line: #c2102c;
    --orange: #f39a10;
    --blue: #1aa3dc;
    --blue-dim: #1b83b5;
    --text: #e8e8e8;
    --muted: #6e7479;
    --panel: #121517;
    --panel-line: #5a5f63;
  }
  * { box-sizing: border-box; margin: 0; padding: 0; }
  html, body { width: 1200px; height: 775px; overflow: hidden; background: var(--black); }
  .canvas {
    position: relative; width: 1200px; height: 775px; overflow: hidden;
    background: radial-gradient(ellipse 700px 500px at 600px 430px, #23282c 0%, var(--page) 70%, #050607 100%);
    font-family: "PT Sans", sans-serif; color: var(--text);
  }
  .topbar { position: absolute; left: 0; top: 0; width: 1200px; height: 70px; background: var(--black); }
  .band {
    position: absolute; left: 0; top: 70px; width: 1200px; height: 80px;
    background: linear-gradient(180deg, var(--red-dark), #4a000c);
  }
  .nav {
    position: absolute; left: 95px; top: 70px; width: 1006px; height: 96px;
    background: linear-gradient(180deg, #b0001f 0%, var(--red) 60%, #8a0018 100%);
    border-top: 2px solid var(--red-line);
  }
  .glow {
    position: absolute; left: 95px; top: 166px; width: 1006px; height: 60px;
    background: linear-gradient(180deg, rgba(150,0,25,0.55), rgba(0,0,0,0));
  }
  .nav-item {
    position: absolute; top: 0; height: 94px; line-height: 94px;
    font-family: "Open Sans", sans-serif; font-size: 13px; font-weight: 600;
    color: #fff; text-transform: uppercase; text-align: center;
  }
  .divider { position: absolute; top: 0; width: 1px; height: 94px; background: rgba(0,0,0,0.25); }
  .utility { position: absolute; left: 170px; top: 37px; }
  .signup {
    position: absolute; left: 973px; top: 0; width: 79px; height: 26px;
    background: var(--orange); color: #fff; font-family: "Open Sans", sans-serif;
    font-size: 12px; font-weight: 700; line-height: 26px; text-align: center;
  }
  .follow {
    position: absolute; left: 872px; top: 37px; width: 180px; height: 38px;
    background: #3b3d3f; border-radius: 3px;
    font-family: "Open Sans", sans-serif; font-size: 11px; font-weight: 700; color: #fff;
    line-height: 38px; padding-left: 10px;
  }
  .social { position: absolute; top: 9px; width: 21px; height: 21px; border-radius: 3px; }
  .social.one { left: 86px; background: #3b5a98; }
  .social.two { left: 117px; background: #6ab8d8; }
  .social.three { left: 148px; background: #e8821a; }
  .brand-mark {
    position: absolute; left: 530px; top: 40px; width: 140px; height: 140px; border-radius: 50%;
    background: radial-gradient(circle at 45% 40%, #d6d6d6, #7c7c7c 70%, #4a4a4a);
  }
  .brand-name {
    position: absolute; left: 0; top: 218px; width: 1200px; text-align: center;
    font-family: "PT Sans", sans-serif; font-weight: 700; font-size: 27px;
    letter-spacing: 2px; color: #c9c9c9; text-transform: uppercase;
  }
  .panel {
    position: absolute; left: 114px; top: 287px; width: 972px; height: 392px;
    border: 1px solid var(--panel-line); border-radius: 7px;
    background: linear-gradient(180deg, #181b1d, var(--panel));
  }
  .headline {
    position: absolute; left: 146px; top: 328px; font-family: "Rokkitt", serif;
    font-size: 35px; line-height: 40px; color: #fff;
  }
  .tagline {
    position: absolute; left: 148px; top: 423px; font-family: "PT Sans", sans-serif;
    font-weight: 700; font-size: 18px; color: var(--blue);
  }
  .copy { position: absolute; left: 148px; width: 440px; font-size: 16px; line-height: 24px; color: #dcdcdc; }
  .copy.first { top: 483px; }
  .copy.second { top: 579px; }
  .hint {
    position: absolute; left: 774px; top: 312px; width: 140px; text-align: center;
    font-family: "Open Sans", sans-serif; font-size: 14px; font-weight: 700; line-height: 20px; color: #fff;
  }
  .arrow { position: absolute; left: 700px; top: 325px; }
  .player {
    position: absolute; left: 626px; top: 384px; width: 428px; height: 244px;
    border: 4px solid #fff; background: #1a1a1a;
  }
  .player-bar {
    position: absolute; left: 0; top: 0; width: 100%; height: 26px; background: #141414;
    font-family: "Open Sans", sans-serif; font-size: 12px; font-weight: 700; color: #9a9a9a; line-height: 26px;
  }
  .player-bar span { position: absolute; top: 0; }
  .video-scene {
    position: absolute; left: 0; top: 26px; width: 100%; height: 184px;
    background: radial-gradient(ellipse at 50% 45%, #f2f2f2 0%, #bdbdbd 55%, #5e5e5e 100%);
  }
  .video-title {
    position: absolute; left: 14px; top: 16px; padding: 4px 8px; background: #111;
    font-family: "Open Sans", sans-serif; font-weight: 700; font-size: 17px; color: #fff;
  }
  .video-source {
    position: absolute; right: 18px; bottom: 16px; font-family: "Open Sans", sans-serif;
    font-weight: 600; font-size: 15px; color: #fff;
  }
  .play-btn { position: absolute; left: 182px; top: 56px; }
  .controls {
    position: absolute; left: 0; bottom: 0; width: 100%; height: 26px; background: #161616;
    font-family: "Open Sans", sans-serif; font-size: 11px; color: #bbb; line-height: 26px;
  }
  .footer-links {
    position: absolute; left: 114px; top: 714px; font-family: "Open Sans", sans-serif;
    font-size: 12px; color: var(--muted); word-spacing: 1px;
  }
  .footer-links .sep { margin: 0 7px; }
  .copyright {
    position: absolute; left: 116px; top: 740px; font-family: "Open Sans", sans-serif;
    font-size: 12px; color: var(--blue-dim);
  }
  .contact {
    position: absolute; left: 828px; top: 700px; font-family: "Didact Gothic", sans-serif;
    font-size: 44px; color: #d0d0d0; letter-spacing: 0.5px;
  }
  .contact-icon { position: absolute; left: 1054px; top: 708px; }
</style>
</head>
<body>
<div class="canvas">
  <div class="topbar"></div>
  <div class="band"></div>
  <nav class="nav">
    <div class="nav-item" style="left:0;width:126px">Company</div>
    <div class="divider" style="left:126px"></div>
    <div class="nav-item" style="left:126px;width:120px">Services</div>
    <div class="divider" style="left:246px"></div>
    <div class="nav-item" style="left:246px;width:120px">Partners</div>
    <div class="divider" style="left:366px"></div>
    <div class="divider" style="left:651px"></div>
    <div class="nav-item" style="left:651px;width:124px">Calendar</div>
    <div class="divider" style="left:775px"></div>
    <div class="nav-item" style="left:775px;width:135px">Resources</div>
    <div class="divider" style="left:910px"></div>
    <div class="nav-item" style="left:910px;width:96px">Blog</div>
  </nav>
  <div class="glow"></div>

  <svg class="utility" width="60" height="20" viewBox="0 0 60 20" aria-hidden="true">
    <path d="M1 9 L8 2 L15 9 M3 8 V15 H13 V8" fill="none" stroke="#bbb" stroke-width="2"/>
    <rect x="29" y="5" width="15" height="10" fill="none" stroke="#bbb" stroke-width="1.6"/>
    <path d="M29 5 L36.5 11 L44 5" fill="none" stroke="#bbb" stroke-width="1.4"/>
  </svg>

  <div class="signup">SIGN UP &#9711;</div>
  <div class="follow">FOLLOW US
    <span class="social one"></span><span class="social two"></span><span class="social three"></span>
  </div>

  <div class="brand-mark"></div>
  <div class="brand-name">Quillstone Ventures</div>

  <div class="panel"></div>
  <h1 class="headline">We are a company<br>that empowers futures.</h1>
  <p class="tagline">Eque porro quisquam est qui dolorem!</p>
  <p class="copy first">Lorem Ipsum is simply dummy text of the printing and typesetting industry. Lorem Ipsum has been the industry's standard dummy text ever since the 1500s.</p>
  <p class="copy second">When an unknown printer took a galley of type and scrambled it to make a type specimen book.</p>

  <div class="hint">click here to<br>watch our intro!</div>
  <svg class="arrow" width="90" height="40" viewBox="0 0 90 40" aria-hidden="true">
    <path d="M72 8 C45 6 22 14 12 32" fill="none" stroke="#f0a81a" stroke-width="2.5"/>
    <path d="M5 30 L12 36 L17 27" fill="none" stroke="#f0a81a" stroke-width="2.5"/>
  </svg>

  <div class="player">
    <div class="player-bar">
      <span style="left:8px">Share &#9662;</span>
      <span style="left:80px;width:1px;height:26px;background:#333"></span>
      <span style="left:88px">No Subtitles &#9662;</span>
      <span style="right:8px;font-size:10px">HD</span>
    </div>
    <div class="video-scene" role="img" aria-label="Intro video still: a radio tower sending signals on a light grey backdrop">
      <div class="video-title">Clip Vault demo</div>
      <svg class="play-btn" width="50" height="58" viewBox="0 0 50 58" aria-hidden="true">
        <path d="M4 2 L48 29 L4 56 Z" fill="#fff" fill-opacity="0.9"/>
      </svg>
      <div class="video-source">StreamHall.tv</div>
    </div>
    <div class="controls">
      <svg width="20" height="26" viewBox="0 0 20 26" style="position:absolute;left:14px;top:0" aria-hidden="true"><path d="M4 7 L16 13 L4 19 Z" fill="#ccc"/></svg>
      <span style="position:absolute;left:50px;width:1px;height:26px;background:#333"></span>
      <span style="position:absolute;left:60px">00:00</span>
      <span style="position:absolute;left:98px;top:9px;width:196px;height:9px;border:1px solid #666;background:#0c0c0c"></span>
      <span style="position:absolute;left:302px">02:23</span>
      <span style="position:absolute;left:342px;top:8px;width:50px;height:10px;border-bottom:1px solid #888"></span>
      <span style="position:absolute;right:10px;font-size:13px">&#10530;</span>
    </div>
  </div>

  <div class="footer-links">About Company<span class="sep">|</span>Our Services<span class="sep">|</span>Hire Us<span class="sep">|</span>Event Calendar<span class="sep">|</span>Free Resources<span class="sep">|</span>Owner Blog</div>
  <div class="copyright">&copy; 2012 QUILLSTONE VENTURES. All Rights Reserved.</div>
  <div class="contact">Contact Us</div>
  <svg class="contact-icon" width="32" height="36" viewBox="0 0 32 36" aria-hidden="true">
    <path d="M2 2 H16 V12 H10 V24 H16 V34 H2 Z" fill="#d0d0d0"/>
    <path d="M13 14 H21 V8 L31 18 L21 28 V22 H13 Z" fill="#d0d0d0"/>
  </svg>
</div>
</body>
</html>
```